PostCard Design Project

We are a landscaping business and offer Landscaping services: Design • Paving and Concreting styles • Pool Copings • Retaining Walls • Plant Supply • Decking • Pergolas • Water Features • Irrigation • Instant Turf • Synthetic Turf Surfaces • and more...

We are looking to create a Postcard - this will be used when we are working on a project and will be dropped into letterboxes of the residents neighbouring the project address. It should be along the lines of: "We apologise for any disturbance you may incur while we are working on your neighbours property." It should also include a 10% discount offer for any services they would like to get done, maybe on the back,, along the lines of" While we are in your area we'd like to offer you a 10% discount on any of our landscaping services" Offer valid for 30 days only. Also maybe a list of servcies on the back as well.

Industry/Entity Type

Landscaping

Requirements
Must have
• Company Logo, and contact details

```html
<!DOCTYPE html>
<html lang="en">
<head>
<meta charset="utf-8">
<title>Fernbrook Landscapes – Neighbour Postcard</title>
<link rel="stylesheet" href="https://fonts.googleapis.com/css2?family=Lora:wght@700&family=Carlito&family=Arimo&display=swap">
<style>
  :root {
    --page-bg: #e6d2b6;
    --card-white: #ffffff;
    --leaf-green: #7cc242;
    --leaf-green-light: #a6d86a;
    --forest-green: #3f7a1e;
    --grid-black: #0d0d0d;
    --footer-grey: #3a3a3a;
  }
  * { margin: 0; padding: 0; box-sizing: border-box; }
  html, body { width: 1200px; height: 900px; overflow: hidden; }
  body { background: var(--page-bg); position: relative; }

  .card {
    position: absolute;
    background: var(--card-white);
    overflow: hidden;
    box-shadow: 0 2px 8px rgba(0,0,0,0.18);
  }
  .card--front { left: 46px; top: 35px; width: 544px; height: 813px; }
  .card--back  { left: 624px; top: 37px; width: 542px; height: 811px; }

  /* ---------- front ---------- */
  .brand {
    position: absolute;
    font-family: "Lora", Georgia, serif;
    font-weight: 700;
    color: var(--leaf-green);
    line-height: 1;
    display: flex;
    align-items: center;
  }
  .brand__dot {
    border-radius: 50%;
    background: var(--leaf-green);
    flex: none;
  }
  .brand__name span { display: block; }

  .front__brand { left: 18px; top: 60px; font-size: 33px; gap: 12px; }
  .front__brand .brand__dot { width: 30px; height: 30px; }

  .offer-art { position: absolute; left: 0; top: 0; width: 544px; height: 190px; }
  .offer-art text { font-family: "Lora", Georgia, serif; font-weight: 700; fill: var(--forest-green); }

  .offer-tail {
    position: absolute;
    left: 254px; top: 153px;
    font-family: "Lora", Georgia, serif;
    font-weight: 700;
    font-size: 18.5px;
    color: var(--forest-green);
    white-space: nowrap;
  }

  .front__rule {
    position: absolute; left: 0; top: 180px; width: 544px; height: 6px;
    background: var(--leaf-green);
  }

  .gallery {
    position: absolute; left: 0; top: 186px; width: 544px; height: 559px;
    background: var(--grid-black);
  }
  .gallery__photo { position: absolute; }
  .photo--sunken   { left: 11px;  top: 10px;  width: 256px; height: 191px; background: linear-gradient(160deg, #8fa86a 0%, #3f7a2a 45%, #6e9a3c 70%, #c8443a 100%); }
  .photo--maples   { left: 277px; top: 10px;  width: 257px; height: 191px; background: linear-gradient(180deg, #c9ccc8 0%, #4c6b3a 35%, #5a3048 60%, #5fae2e 100%); }
  .photo--steps    { left: 11px;  top: 211px; width: 256px; height: 169px; background: linear-gradient(135deg, #4a6a2c 0%, #7d8a3c 40%, #c2546a 70%, #2f4a1c 100%); }
  .photo--woodland { left: 277px; top: 211px; width: 257px; height: 169px; background: linear-gradient(180deg, #2d4a22 0%, #5c7a3a 45%, #7fb640 70%, #3a5a28 100%); }
  .photo--parterre { left: 11px;  top: 390px; width: 256px; height: 159px; background: linear-gradient(150deg, #2f5a24 0%, #4f8a32 40%, #4a3a6a 65%, #3d7a2a 100%); }
  .photo--grass    { left: 277px; top: 390px; width: 257px; height: 159px; background: linear-gradient(120deg, #3f6a12 0%, #8cc21e 45%, #c6e040 65%, #4f7a16 100%); }

  .front__footer {
    position: absolute; left: 0; top: 745px; width: 544px; height: 68px;
    background: linear-gradient(180deg, var(--leaf-green-light) 0%, var(--leaf-green) 100%);
    color: #ffffff;
    font-family: "Carlito", "Calibri", sans-serif;
    font-size: 18.5px;
    line-height: 24px;
    text-align: center;
    padding-top: 9px;
  }

  /* ---------- back ---------- */
  .back__brand { left: 118px; top: 60px; font-size: 50px; gap: 18px; }
  .back__brand .brand__dot { width: 46px; height: 46px; }

  .services {
    position: absolute; left: 98px; top: 265px;
    list-style: none;
    font-family: "Carlito", "Calibri", sans-serif;
    font-size: 23px;
    color: var(--leaf-green);
  }
  .services li {
    height: 34px; line-height: 34px;
    display: flex; align-items: center; gap: 28px;
  }
  .services__mark {
    width: 12px; height: 8px; flex: none;
    border-radius: 6px 6px 2px 2px;
    background: var(--leaf-green);
  }

  .back__rule {
    position: absolute; left: 0; top: 716px; width: 542px; height: 5px;
    background: var(--leaf-green);
  }
  .back__footer {
    position: absolute; left: 0; top: 726px; width: 542px; height: 85px;
    background: linear-gradient(180deg, var(--leaf-green-light) 0%, var(--leaf-green) 55%, #6aae34 100%);
    font-family: "Arimo", Arial, sans-serif;
    font-size: 19.5px;
    color: var(--footer-grey);
    padding: 32px 0 0 66px;
    white-space: pre;
  }
</style>
</head>
<body>

<section class="card card--front" aria-label="Postcard front">
  <div class="brand front__brand">
    <span class="brand__dot"></span>
    <span class="brand__name"><span>Fernbrook</span><span>Landscapes</span></span>
  </div>

  <svg class="offer-art" viewBox="0 0 544 190" aria-label="While we are in your area we'd like to offer you a 10% discount">
    <defs>
      <path id="offer-arc-1" d="M252 62 Q385 -2 528 64"/>
      <path id="offer-arc-2" d="M310 76 Q385 48 462 76"/>
      <linearGradient id="sticker-fill" x1="0" y1="0" x2="1" y2="1">
        <stop offset="0" stop-color="#9fd45e"/>
        <stop offset="1" stop-color="#4f9a22"/>
      </linearGradient>
    </defs>
    <text font-size="19.5"><textPath href="#offer-arc-1" startOffset="50%" text-anchor="middle">While we are in your area we’d</textPath></text>
    <text font-size="18"><textPath href="#offer-arc-2" startOffset="50%" text-anchor="middle">like to offer you a</textPath></text>
    <circle cx="382" cy="112" r="40" fill="url(#sticker-fill)"/>
    <g transform="rotate(-28 382 112)" fill="#ffffff" text-anchor="middle">
      <text x="382" y="108" font-size="21" style="fill:#ffffff">10%</text>
      <text x="384" y="126" font-size="12" style="fill:#ffffff;font-family:Arimo, Arial, sans-serif">DISCOUNT</text>
    </g>
  </svg>

  <p class="offer-tail">of our Landscaping Services</p>
  <div class="front__rule"></div>

  <div class="gallery">
    <div class="gallery__photo photo--sunken" role="img" aria-label="Photo of a sunken garden with winding paths and flower beds"></div>
    <div class="gallery__photo photo--maples" role="img" aria-label="Photo of purple maple trees on a green lawn"></div>
    <div class="gallery__photo photo--steps" role="img" aria-label="Photo of stone steps through pink azaleas"></div>
    <div class="gallery__photo photo--woodland" role="img" aria-label="Photo of a woodland garden with tall trunks and lawn"></div>
    <div class="gallery__photo photo--parterre" role="img" aria-label="Photo of a formal hedge parterre with a fountain"></div>
    <div class="gallery__photo photo--grass" role="img" aria-label="Close-up photo of bright green grass blades"></div>
  </div>

  <p class="front__footer">we apologise for any disturbance you may incur<br>while we are working on your neighbours property</p>
</section>

<section class="card card--back" aria-label="Postcard back">
  <div class="brand back__brand">
    <span class="brand__dot"></span>
    <span class="brand__name"><span>Fernbrook</span><span>Landscapes</span></span>
  </div>

  <ul class="services">
    <li><span class="services__mark"></span>Design</li>
    <li><span class="services__mark"></span>Paving and Concreting styles</li>
    <li><span class="services__mark"></span>Pool Copings</li>
    <li><span class="services__mark"></span>Retaining Walls</li>
    <li><span class="services__mark"></span>Plant Supply</li>
    <li><span class="services__mark"></span>Decking</li>
    <li><span class="services__mark"></span>Pergolas</li>
    <li><span class="services__mark"></span>Water Features</li>
    <li><span class="services__mark"></span>Irrigation</li>
    <li><span class="services__mark"></span>Instant Turf</li>
    <li><span class="services__mark"></span>Synthetic Turf Surfaces</li>
    <li><span class="services__mark"></span>and more...</li>
  </ul>

  <div class="back__rule"></div>
  <p class="back__footer">Fernbrook Landscapes, Marcus    Ph : 0432 718</p>
</section>

</body>
</html>
```